TKR Engineering Pty Ltd

I have already had nox welding and fabrication cards made , my business has changed too TKR engineering Pty Ltd so I need my logo changed on the cards
one side have my logo then the other side have what we do.
front side logo and details
owner /operator : Curtis Halvorsen
email: tkr.works@examplemail.net
number: 0491537204
ABN: 52 604 381 927
ACN: 728 391 056
on back have in dot points what we do:
* structural steel erection
* precast panels
* site welding
*steel alteration & repair
* rigging & dogging
*labour hire
Contact Information for Business Card
all details in breif
Look and feel
Each slider illustrates characteristics of the customer's brand and the style your logo design should communicate.

```html
<!DOCTYPE html>
<html lang="en">
<head>
<meta charset="UTF-8">
<title>TKR Engineering Pty Ltd – Business Card</title>
<link rel="stylesheet" href="https://fonts.googleapis.com/css2?family=Poppins:wght@400;600&display=swap">
<style>
  :root {
    --navy: #13213a;
    --rust: #8e4238;
    --white: #ffffff;
    --ink: #1d2433;
    --backdrop: #bdbdbd;
    --card-w: 742px;
    --card-h: 424px;
  }
  * { box-sizing: border-box; margin: 0; padding: 0; }
  html, body {
    width: 1200px;
    height: 1200px;
    overflow: hidden;
    background: var(--backdrop);
    font-family: "Poppins", sans-serif;
  }
  .card {
    position: absolute;
    left: 229px;
    width: var(--card-w);
    height: var(--card-h);
    overflow: hidden;
  }
  .card--front { top: 136px; background: var(--white); }
  .card--back { top: 641px; background: var(--navy); }

  /* Front */
  .front-tab {
    position: absolute;
    left: 0; top: 190px;
    width: 9px; height: 46px;
    background: var(--navy);
    border-radius: 0 5px 5px 0;
  }
  .brand {
    position: absolute;
    text-align: center;
  }
  .brand__name {
    font-weight: 600;
    line-height: 1.1;
    letter-spacing: 0.5px;
  }
  .brand__phone {
    margin-top: 8px;
    font-weight: 600;
    color: var(--rust);
    letter-spacing: 1.5px;
  }
  .card--front .brand { left: 460px; top: 60px; width: 260px; }
  .card--front .brand__name { color: var(--navy); font-size: 30px; }
  .card--front .brand__phone { font-size: 13px; }

  .person { position: absolute; left: 24px; top: 184px; }
  .person__name { color: var(--rust); font-weight: 600; font-size: 28px; line-height: 1.2; }
  .person__role { color: var(--ink); font-size: 17px; line-height: 1.3; }

  .contacts { position: absolute; left: 26px; top: 256px; list-style: none; }
  .contacts li {
    display: flex; align-items: center; gap: 6px;
    color: var(--ink); font-size: 17px; line-height: 21px;
  }
  .contacts svg { width: 12px; height: 12px; flex: none; }

  .registry { position: absolute; left: 25px; top: 334px; }
  .registry p { color: var(--ink); font-size: 17px; line-height: 24px; }
  .registry span { color: var(--rust); font-weight: 600; }

  .front-band { position: absolute; left: 0; bottom: 0; width: 100%; height: 27px; }

  /* Back */
  .card--back .brand { left: 190px; top: 120px; width: 362px; }
  .card--back .brand__name { color: var(--white); font-size: 38px; }
  .card--back .brand__phone { font-size: 15px; }

  .services__title {
    position: absolute; left: 0; top: 319px; width: 100%;
    text-align: center; color: var(--white);
    font-weight: 600; font-size: 18px;
  }
  .services {
    position: absolute; left: 0; top: 351px; width: 100%; height: 52px;
    background: var(--rust);
    display: flex; flex-direction: column; justify-content: center; align-items: center;
  }
  .services__row {
    list-style: none; display: flex;
    color: var(--white); font-size: 17px; line-height: 23px; text-transform: uppercase;
  }
  .services__row li + li::before {
    content: "";
    display: inline-block;
    width: 2px; height: 12px;
    background: var(--navy);
    margin: 0 9px;
    vertical-align: -1px;
  }
</style>
</head>
<body>

<section class="card card--front" aria-label="Business card front">
  <div class="front-tab"></div>

  <div class="brand">
    <p class="brand__name">TKR Engineering Pty Ltd</p>
    <p class="brand__phone">0491537204</p>
  </div>

  <div class="person">
    <h1 class="person__name">Curtis Halvorsen</h1>
    <p class="person__role">Owner &amp; Operator</p>
  </div>

  <ul class="contacts">
    <li>
      <svg viewBox="0 0 12 12" aria-hidden="true"><rect x="2.5" y="0.8" width="7" height="10.4" rx="1.4" fill="none" stroke="#8e4238" stroke-width="1.4"/><rect x="5" y="8.6" width="2" height="1.2" fill="#8e4238"/></svg>
      +049-1537-204
    </li>
    <li>
      <svg viewBox="0 0 12 12" aria-hidden="true"><rect x="0.5" y="2" width="11" height="8" fill="#8e4238"/><path d="M0.5 2.5 L6 6.5 L11.5 2.5" fill="none" stroke="#fff" stroke-width="1"/></svg>
      tkr.works@examplemail.net
    </li>
    <li>
      <svg viewBox="0 0 12 12" aria-hidden="true"><circle cx="6" cy="6" r="5" fill="none" stroke="#8e4238" stroke-width="1"/><ellipse cx="6" cy="6" rx="2.2" ry="5" fill="none" stroke="#8e4238" stroke-width="0.8"/><path d="M1 6 H11 M1.8 3.5 H10.2 M1.8 8.5 H10.2" stroke="#8e4238" stroke-width="0.8"/></svg>
      www.tkrworks.example.net
    </li>
  </ul>

  <div class="registry">
    <p><span>ACN</span> 728 391 056</p>
    <p><span>ABN</span> 52 604 381 927</p>
  </div>

  <svg class="front-band" viewBox="0 0 742 27" preserveAspectRatio="none" aria-hidden="true">
    <polygon points="0,0 430,0 424,27 0,27" fill="#13213a"/>
    <polygon points="435,0 742,0 742,27 429,27" fill="#8e4238"/>
  </svg>
</section>

<section class="card card--back" aria-label="Business card back">
  <div class="brand">
    <p class="brand__name">TKR Engineering Pty Ltd</p>
    <p class="brand__phone">0491537204</p>
  </div>

  <h2 class="services__title">WHAT WE DO:</h2>
  <div class="services">
    <ul class="services__row">
      <li>Structural Steel Erection</li>
      <li>Precast Panels</li>
      <li>Site Welding</li>
    </ul>
    <ul class="services__row">
      <li>Steel Alteration &amp; Repair</li>
      <li>Rigging &amp; Dogging</li>
      <li>Labour Hire</li>
    </ul>
  </div>
</section>

</body>
</html>
```